Property management company looking for modern card design

We at Blue Heron Partners provides property management services for its residential and commercial properties, with expertise in all categories of multifamily, industrial and office projects throughout California.

We need a business card design that is professional and modern designed business card. In our field, clients get hundreds of business cards, we would like our card to stand out.

Please avoid small print.

Target Market(s)

Professionals and high end clients

Industry/Entity Type

Financial Planning

Contact Information for Business Card

Company Name: Blue Heron Partners, Name, email, license #, phone number, website blueheronpartners.com

Font styles to use
Sans Serif

Requirements
Must have
• The card design needs to be adaptable because there is a possibly we will be expanding into different sectors other than real estate. The card design should be focused on financial planning and asset management.
Nice to have
• Modern and simple business card. Eye catching. Non-standard size/shaped cards would be great.
• blueheronpartners.com
Should not have
• Too many bright color or any pictures or shapes of real estate stuff.

```html
<!DOCTYPE html>
<html lang="en">
<head>
<meta charset="utf-8">
<title>Blue Heron Partners – Business Card</title>
<link href="https://fonts.googleapis.com/css2?family=Montserrat:wght@500;600&family=Questrial&display=swap" rel="stylesheet">
<style>
  :root {
    --backdrop: #869a98;
    --navy: #161a2d;
    --brand-red: #ee1020;
    --ribbon-red: #ff0020;
    --deep-red: #6b0008;
    --paper: #f8f8fc;
    --ink: #161a2d;
  }
  html, body {
    margin: 0;
    width: 1200px;
    height: 1200px;
    overflow: hidden;
    background: var(--backdrop);
  }
  .canvas {
    position: relative;
    width: 1200px;
    height: 1200px;
  }
  .card {
    position: absolute;
    left: 244px;
    width: 666px;
    height: 382px;
    display: block;
  }
  .card--front { top: 146px; }
  .card--back { top: 636px; }
  .brand-name {
    font-family: "Montserrat", sans-serif;
    font-weight: 600;
    fill: var(--brand-red);
  }
  .holder-name {
    font-family: "Montserrat", sans-serif;
    font-weight: 500;
    font-size: 30px;
    letter-spacing: 2px;
    fill: var(--ink);
  }
  .contact-label {
    font-family: "Questrial", sans-serif;
    font-size: 26px;
    fill: var(--ink);
  }
  .icon-disc { fill: var(--deep-red); }
  .icon-line { fill: none; stroke: var(--paper); stroke-width: 1.6; stroke-linecap: round; stroke-linejoin: round; }
</style>
</head>
<body>
<main class="canvas">

  <svg class="card card--front" viewBox="0 0 666 382" aria-label="Card front">
    <rect class="card-base" width="666" height="382" fill="var(--navy)"/>
    <circle class="brand-disc" cx="333" cy="158" r="78" fill="var(--brand-red)"/>
    <text class="brand-name" x="333" y="294" text-anchor="middle" font-size="32" letter-spacing="5">BLUE HERON PARTNERS</text>
    <rect class="base-band" x="0" y="343" width="666" height="39" fill="var(--deep-red)"/>
  </svg>

  <svg class="card card--back" viewBox="0 0 666 382" aria-label="Card back">
    <rect class="card-base" width="666" height="382" fill="var(--navy)"/>
    <polygon class="info-panel" points="474,0 666,0 666,382 334,382" fill="var(--paper)"/>

    <circle class="brand-disc" cx="188" cy="160" r="54" fill="var(--brand-red)"/>
    <text class="brand-name" x="188" y="256" text-anchor="middle" font-size="20" letter-spacing="2">BLUE HERON PARTNERS</text>

    <polygon class="ribbon-fold" points="386,124 428,124 418,154" fill="var(--deep-red)"/>
    <polygon class="name-ribbon" points="386,84 666,86 666,126 386,124" fill="var(--ribbon-red)"/>
    <text class="holder-name" x="460" y="116">Name</text>

    <g class="contact contact--phone">
      <circle class="icon-disc" cx="423" cy="206" r="18"/>
      <path class="icon-line" d="M416,197 l4,-2 3,6 -3,2 q2,5 6,8 l2,-3 6,3 -2,4 q-11,-2 -16,-18z" fill="var(--paper)" stroke="none"/>
      <text class="contact-label" x="464" y="215">Phone</text>
    </g>
    <g class="contact contact--address">
      <circle class="icon-disc" cx="420" cy="256" r="18"/>
      <path class="icon-line" d="M420,270 q-10,-11 -10,-18 a10,10 0 0 1 20,0 q0,7 -10,18z"/>
      <circle class="icon-line" cx="420" cy="252" r="4"/>
      <text class="contact-label" x="464" y="265">Address</text>
    </g>
    <g class="contact contact--web">
      <circle class="icon-disc" cx="420" cy="309" r="18"/>
      <circle class="icon-line" cx="420" cy="309" r="10"/>
      <ellipse class="icon-line" cx="420" cy="309" rx="4.5" ry="10"/>
      <path class="icon-line" d="M410,309 h20 M412,304 h16 M412,314 h16"/>
      <text class="contact-label" x="464" y="318">Internet</text>
    </g>
  </svg>

</main>
</body>
</html>
```